DOUBLE SIDED BROCHURE NEEDED TO PROMOTE DOCTOR

I need a double sided DL size (99mm x 210mm) brochure, promoting a doctor seeing patients in a new area.

I want something professional. I have included the relevant information. I would also like the Dr's picture somwhere in the brochure, with a professional background. I wish to print these tomorrow, so i will pick a winner within 14 hours of posting this ad.

I have included an example of a brochures design that I recently saw, and its definietly a good starting point.

Medical

```html
<!DOCTYPE html>
<html lang="en">
<head>
<meta charset="utf-8">
<title>Dr. Halvorsen – Westhaven Clinic</title>
<link href="https://fonts.googleapis.com/css2?family=Josefin+Sans:wght@700&family=Cabin:wght@700&family=Alegreya+Sans:wght@700&display=swap" rel="stylesheet">
<style>
  :root{
    --sky:#1ab8e8;
    --panel:#70d1ef;
    --navy:#0e2b48;
    --white:#ffffff;
    --wedge:#c9ccd0;
    --photo-top:#8fc3ea;
    --photo-mid:#b9c9d6;
    --photo-low:#5d6670;
  }
  html,body{margin:0;padding:0;overflow:hidden;}
  body{width:1200px;height:2542px;background:var(--white);}
  .brochure{position:relative;width:1200px;height:2542px;background:var(--sky);overflow:hidden;}
  .hero{position:absolute;left:0;top:0;}
  .headline-panel{
    position:absolute;left:207px;top:1724px;width:993px;height:378px;
    background:var(--panel);
    box-shadow:0 7px 6px rgba(10,40,70,.45);
  }
  .headline{
    margin:0;position:absolute;right:18px;top:38px;
    font-family:"Josefin Sans",sans-serif;font-weight:700;
    font-size:72px;line-height:105px;letter-spacing:1px;
    color:var(--navy);text-align:right;white-space:nowrap;
  }
  .headline span{display:block;height:105px;}
  .clinic{
    position:absolute;right:22px;top:2192px;text-align:right;color:var(--navy);
  }
  .clinic-title{
    margin:0 0 22px;font-family:"Cabin",sans-serif;font-weight:700;
    font-size:54px;line-height:62px;white-space:nowrap;
  }
  .clinic-address{
    margin:0;font-family:"Alegreya Sans",sans-serif;font-weight:700;
    font-size:60px;line-height:63px;font-style:normal;white-space:nowrap;
  }
  .corner-wedge{position:absolute;right:0;bottom:0;}
  .referral-note{
    position:absolute;left:46px;bottom:22px;margin:0;white-space:nowrap;
    font-family:"Cabin",sans-serif;font-weight:700;font-size:39px;line-height:46px;
    color:var(--white);text-shadow:2px 2px 2px rgba(0,0,0,.75);
  }
</style>
</head>
<body>
<main class="brochure">
  <svg class="hero" width="1200" height="1720" viewBox="0 0 1200 1720">
    <defs>
      <linearGradient id="photoTone" x1="0" y1="0" x2="0" y2="1">
        <stop offset="0" stop-color="var(--photo-top)"/>
        <stop offset="0.35" stop-color="var(--photo-mid)"/>
        <stop offset="1" stop-color="var(--photo-low)"/>
      </linearGradient>
      <clipPath id="heroClip"><ellipse cx="340" cy="780" rx="790" ry="966"/></clipPath>
    </defs>
    <ellipse cx="340" cy="780" rx="830" ry="1003" fill="var(--white)"/>
    <g clip-path="url(#heroClip)">
      <rect x="0" y="0" width="1200" height="1720" fill="url(#photoTone)"
            role="img" aria-label="Portrait of the doctor smiling in front of a modern hospital building under a cloudy blue sky"/>
    </g>
  </svg>

  <section class="headline-panel">
    <h1 class="headline"><span>DR.HALVORSEN IS NOW</span><span>CONSULTING IN</span><span>WESTHAVEN</span></h1>
  </section>

  <svg class="corner-wedge" width="250" height="195" viewBox="0 0 250 195" aria-hidden="true">
    <polygon points="250,0 250,195 0,195" fill="var(--wedge)"/>
  </svg>

  <section class="clinic">
    <h2 class="clinic-title">WESTHAVEN CLINIC:</h2>
    <address class="clinic-address">
      42 Larkspur Road<br>
      Westhaven WA 6999.<br>
      Phone: 1300 482 107
    </address>
  </section>

  <p class="referral-note">PLEASE SEND ALL REFERRALS BY FAX TO (08) 5550 2846</p>
</main>
</body>
</html>
```